Stationary Design

Harbor Stage Works, Inc
27450 Mariner Ave Ste 3, Bayside Springs, CA 90799
Office: 213-555-0847 Email: admin@hswinc.example

Industry/Entity Type

Entertainment

Colors
0054AA
0677BA
7BADD7
CADEEF
E8F1F8

```html
<!DOCTYPE html>
<html lang="en">
<head>
<meta charset="utf-8">
<title>Harbor Stage Works — Stationery</title>
<link rel="stylesheet" href="https://fonts.googleapis.com/css2?family=Lato:wght@400;700&display=swap">
<style>
  :root {
    --brand-blue: #2257ab;
    --brand-blue-deep: #0054aa;
    --brand-grey: #9a9a9a;
    --text-grey: #5a5a5a;
    --ink: #222;
    --paper: #ffffff;
    --backdrop: #e9ecef;
    --tint: #e8f1f8;
  }
  * { box-sizing: border-box; margin: 0; padding: 0; }
  html, body { width: 1200px; height: 1200px; overflow: hidden; }
  body {
    position: relative;
    background: var(--backdrop);
    font-family: "Lato", sans-serif;
    color: var(--ink);
  }

  /* Letterhead */
  .letterhead {
    position: absolute; left: 268px; top: 170px; width: 667px; height: 863px;
    background: var(--paper);
    box-shadow: 4px 6px 14px rgba(0,0,0,.25);
    overflow: hidden;
  }
  .letterhead .brand {
    position: absolute; left: 142px; top: 40px; width: 181px; height: 96px;
    display: flex; flex-direction: column; align-items: center; justify-content: center; gap: 10px;
  }
  .brand-dot { border-radius: 50%; border: 6px solid var(--brand-blue); }
  .letterhead .brand-dot { width: 56px; height: 56px; }
  .brand-name { color: var(--brand-blue); font-weight: 700; text-align: center; line-height: 1.1; white-space: nowrap; }
  .letterhead .brand-name { font-size: 15px; }
  .letterhead .divider {
    position: absolute; left: 332px; top: 41px; width: 1px; height: 92px; background: var(--brand-grey);
  }
  .letterhead .contact { position: absolute; left: 354px; top: 36px; }
  .letterhead .company { color: var(--brand-blue); font-weight: 700; font-size: 14px; margin-bottom: 2px; }
  .letterhead .address { color: var(--text-grey); font-size: 12.5px; line-height: 14.5px; margin-bottom: 6px; }
  .contact-line { display: flex; align-items: center; gap: 5px; color: var(--text-grey); }
  .letterhead .contact-line { font-size: 12.5px; height: 17.5px; }
  .icon { flex: none; fill: none; stroke: var(--brand-blue); stroke-width: 2; }
  .letterhead .icon { width: 8px; height: 8px; }
  .watermark {
    position: absolute; left: -60px; top: 405px; width: 400px; height: 400px;
    border-radius: 50%; border: 40px solid var(--tint); opacity: .7;
  }

  .footer-band { position: absolute; left: 0; right: 0; bottom: 0; }
  .footer-band svg { display: block; width: 100%; height: 100%; }
  .letterhead .footer-band { height: 15px; }

  /* Business cards */
  .card {
    position: absolute; top: 358px; width: 351px; height: 200px;
    box-shadow: 4px 6px 12px rgba(0,0,0,.3);
    overflow: hidden;
  }
  .card-front { left: 92px; background: var(--paper); }
  .card-front .brand {
    position: absolute; left: 24px; top: 52px; width: 150px; height: 86px;
    display: flex; flex-direction: column; align-items: center; justify-content: center; gap: 9px;
  }
  .card-front .brand-dot { width: 48px; height: 48px; border-width: 5px; }
  .card-front .brand-name { font-size: 12.5px; }
  .card-front .divider {
    position: absolute; left: 194px; top: 48px; width: 1px; height: 99px; background: var(--brand-grey);
  }
  .card-front .details { position: absolute; left: 207px; top: 46px; }
  .person-name { color: var(--brand-blue); font-weight: 700; font-size: 13.5px; }
  .person-role { font-size: 8px; margin-bottom: 8px; }
  .card-front .address { font-size: 8px; line-height: 10.5px; margin-bottom: 6px; }
  .card-front .contact-line { font-size: 8px; height: 11px; color: var(--ink); gap: 6px; }
  .card-front .icon { width: 6px; height: 6px; }
  .card-front .footer-band { height: 5px; }

  .card-back { left: 781px; background: var(--brand-blue); }
  .pattern-field { position: absolute; inset: 0; background: linear-gradient(135deg, #2a5fb3, #1f52a3); }
  .card-back .brand {
    position: absolute; left: 0; right: 0; top: 72px;
    display: flex; flex-direction: column; align-items: center; gap: 8px;
  }
  .card-back .brand-dot { width: 44px; height: 44px; border: 5px solid var(--paper); }
  .card-back .brand-name { color: var(--paper); font-size: 11.5px; }
</style>
</head>
<body>

<section class="letterhead">
  <div class="watermark"></div>
  <div class="brand">
    <span class="brand-dot"></span>
    <span class="brand-name">HARBOR STAGE WORKS</span>
  </div>
  <div class="divider"></div>
  <div class="contact">
    <p class="company">Harbor Stage Works, Inc</p>
    <p class="address">27450 Mariner Ave Ste 3<br>Bayside Springs, CA 90799</p>
    <p class="contact-line"><svg class="icon" viewBox="0 0 10 10"><path d="M2 1l2 2-1 1.5c.7 1.3 1.2 1.8 2.5 2.5L7 6l2 2-1.5 1.5C4 9 1 6 .5 2.5z" fill="#2257ab" stroke="none"/></svg>213-555-0847</p>
    <p class="contact-line"><svg class="icon" viewBox="0 0 10 10"><rect x="1" y="2" width="8" height="6"/><path d="M1 2l4 3 4-3"/></svg>admin@hswinc.example</p>
    <p class="contact-line"><svg class="icon" viewBox="0 0 10 10"><circle cx="5" cy="5" r="4"/><path d="M1 5h8M5 1c-2 2.5-2 5.5 0 8M5 1c2 2.5 2 5.5 0 8"/></svg>www.hswinc.example</p>
  </div>
  <div class="footer-band">
    <svg viewBox="0 0 667 15" preserveAspectRatio="none">
      <rect x="0" y="0" width="667" height="15" fill="#9a9a9a"/>
      <path d="M0 0H508L490 15H0z" fill="#2257ab"/>
      <path d="M508 0L490 15H498L514 2Q520 0 530 0z" fill="#fff"/>
    </svg>
  </div>
</section>

<section class="card card-front">
  <div class="brand">
    <span class="brand-dot"></span>
    <span class="brand-name">HARBOR STAGE WORKS</span>
  </div>
  <div class="divider"></div>
  <div class="details">
    <p class="person-name">Dana Whitfield</p>
    <p class="person-role">Founder &amp; CEO</p>
    <p class="address">27450 Mariner Ave Ste 3<br>Bayside Springs<br>CA 90799</p>
    <p class="contact-line"><svg class="icon" viewBox="0 0 10 10"><path d="M2 1l2 2-1 1.5c.7 1.3 1.2 1.8 2.5 2.5L7 6l2 2-1.5 1.5C4 9 1 6 .5 2.5z" fill="#2257ab" stroke="none"/></svg>213-555-0847</p>
    <p class="contact-line"><svg class="icon" viewBox="0 0 10 10"><rect x="1" y="2" width="8" height="6"/><path d="M1 2l4 3 4-3"/></svg>admin@hswinc.example</p>
    <p class="contact-line"><svg class="icon" viewBox="0 0 10 10"><circle cx="5" cy="5" r="4"/><path d="M1 5h8M5 1c-2 2.5-2 5.5 0 8M5 1c2 2.5 2 5.5 0 8"/></svg>www.hswinc.example</p>
  </div>
  <div class="footer-band">
    <svg viewBox="0 0 351 5" preserveAspectRatio="none">
      <rect x="0" y="0" width="351" height="5" fill="#9a9a9a"/>
      <path d="M0 0H253L246 5H0z" fill="#2257ab"/>
      <path d="M253 0L246 5H250L257 0z" fill="#fff"/>
    </svg>
  </div>
</section>

<section class="card card-back">
  <div class="pattern-field" role="img" aria-label="Embossed repeating brand pattern on blue"></div>
  <div class="brand">
    <span class="brand-dot"></span>
    <span class="brand-name">HARBOR STAGE WORKS</span>
  </div>
</section>

</body>
</html>
```